Skill Up Salary Up

Full Page
7.5 w x 10 h / 8 w x 10.75 h + .25" bleed
Full-Page Career Course Ad
Project Overview
• Goal: Create a visually attractive, modern, and uncluttered full-page magazine advertisement to list available career courses.
• Tone: Creative, professional, and attention-grabbing to prevent the reader from turning the page. The final design must prioritize readability.

Content Requirements
1. Header/Headline: Must be the primary focus. And grab peoples attention
2. Course Listing: A clear, well-organized list of the career courses.
________________________________________
Design & Aesthetic Directives
1. Layout & Readability (Crucial)
• The final ad must not look crowded or busy.
• Prioritize white space to make the text "breathe" and ensure the course list is easy to scan and read.
• Use a modern, clean, and professional typeface (font choice is critical for the aesthetic).
2. Visual Style
• Aim for a creative, modern, and fresh look. Avoid outdated or generic stock imagery/layouts.
3. Imagery/Graphic Element (Artist's Choice)
You have creative freedom regarding the main graphic element.
• Option A (Photography): Use a photo of a white male American with a collared shirt. The imagery should convey success, focus, or professional development.
• Option B (Vector/Illustration): Use a modern vector graphic, illustration, or abstract design. This could be used to symbolize growth, connection, or a career path.
The choice of graphic element is yours, but it must support the overall modern and uncrowded aesthetic.

Requirements
Must have
• Partial listing .. is part of the Harbor Lantern Course

```html
<!DOCTYPE html>
<html lang="en">
<head>
<meta charset="utf-8">
<title>Skill Up, Salary Up — Bayline Courses</title>
<link href="https://fonts.googleapis.com/css2?family=Barlow+Semi+Condensed:wght@700;800&family=Roboto+Condensed:wght@400;500;600;700&display=swap" rel="stylesheet">
<style>
  :root{
    --navy:#1c4a78;
    --ink:#1d3f66;
    --cream:#fcf7f1;
    --teal:#2bbccc;
    --pink:#e0247a;
    --orange:#f26b3a;
    --white:#ffffff;
    --page:#ffffff;
  }
  *{margin:0;padding:0;box-sizing:border-box}
  html,body{width:849px;height:1200px;overflow:hidden;background:var(--page)}
  body{position:relative;font-family:"Roboto Condensed",sans-serif;color:var(--ink)}
  .abs{position:absolute;line-height:1;white-space:nowrap}

  .ad{position:absolute;left:53px;top:43px;width:742px;height:1113px;
    background:
      radial-gradient(ellipse 70% 55% at 0% 0%, #fcd877 0%, rgba(252,216,119,0) 70%),
      radial-gradient(ellipse 70% 50% at 100% 100%, #4a82c6 0%, rgba(74,130,198,0) 70%),
      linear-gradient(115deg,#f7b565 0%,#f08a6e 25%,#e9578a 55%,#d04a94 72%,#7a55a6 100%);}

  .headline{left:0;width:849px;top:80px;text-align:center;
    font-family:"Barlow Semi Condensed",sans-serif;font-weight:800;font-size:76px;
    color:var(--navy);letter-spacing:-0.5px}
  .subhead{left:0;width:849px;top:162px;text-align:center;
    font-family:"Barlow Semi Condensed",sans-serif;font-weight:800;font-size:38px;
    color:var(--navy);letter-spacing:1.5px}

  .info-pill{position:absolute;left:105px;top:215px;width:633px;height:85px;border-radius:14px;
    background:linear-gradient(90deg,#39bcc8,#22bdd2)}
  .info-line{left:105px;width:633px;text-align:center;
    font-family:"Barlow Semi Condensed",sans-serif;font-weight:700;font-size:28px;color:var(--white)}

  .card{position:absolute;left:100px;top:320px;width:651px;height:831px;
    background:var(--cream);border-radius:14px;overflow:hidden}
  .band{position:absolute;left:0;height:60px}
  .band-lantern{top:0;width:651px;background:linear-gradient(90deg,#e0207a 0%,#d22a82 45%,#a03b98 75%,#3553a8 100%)}
  .band-books{top:282px;width:406px;background:var(--navy);border-radius:10px 10px 0 0}
  .band-office{top:584px;width:651px;background:var(--teal)}
  .band-title{font-family:"Roboto Condensed",sans-serif;font-weight:600;font-size:34px;color:var(--white);letter-spacing:-0.3px}

  .lead{font-weight:600;font-size:24px;color:var(--ink)}
  .item{font-weight:400;font-size:24.5px;color:var(--ink)}
  .meta{font-weight:600;font-size:25.5px;color:var(--ink)}
  .topic-title{font-weight:700;font-size:27px;color:var(--ink)}
  .topic{font-weight:400;font-size:25px;color:var(--ink)}
  .dot{position:absolute;width:6px;height:6px;border-radius:50%;background:var(--ink)}
  .dot-pink{background:var(--pink)}
  .dot-orange{background:var(--orange)}
  .icon{position:absolute}

  .app-row{position:absolute;left:121px;top:1019px;display:flex;align-items:center;gap:22px;
    font-weight:400;font-size:24.5px;line-height:1;white-space:nowrap;color:var(--ink)}
  .app{display:flex;align-items:center}
  .app-bullet::before{content:"";width:6px;height:6px;border-radius:50%;background:var(--ink);margin:0 11px 0 3px}
</style>
</head>
<body>
  <div class="ad"></div>

  <h1 class="abs headline">SKILL UP, SALARY UP</h1>
  <h2 class="abs subhead">UPCOMING BAYLINE COURSES</h2>

  <div class="info-pill"></div>
  <p class="abs info-line" style="top:227px">FOR MEN &amp; WOMEN | IN-PERSON &amp; REMOTE</p>
  <p class="abs info-line" style="top:262px">PARTIAL SCHOLARSHIPS AVAILABLE</p>

  <div class="card">
    <div class="band band-lantern"></div>
    <div class="band band-books"></div>
    <div class="band band-office"></div>
  </div>

  <!-- Harbor Lantern Course -->
  <h3 class="abs band-title" style="left:120px;top:335px">Harbor Lantern Course</h3>
  <p class="abs lead" style="left:121px;top:401px">Gain Business Skills &amp; Knowledge to:</p>
  <span class="dot dot-pink" style="left:124px;top:448px"></span>
  <p class="abs item" style="left:144px;top:439px">Impress Your Interviewer</p>
  <span class="dot dot-orange" style="left:124px;top:482px"></span>
  <p class="abs item" style="left:144px;top:473px">Maximize Income</p>
  <span class="dot dot-orange" style="left:124px;top:516px"></span>
  <p class="abs item" style="left:144px;top:507px">Start / Run Your Own Business</p>
  <svg class="icon" style="left:123px;top:555px" width="22" height="22" viewBox="0 0 22 22" aria-hidden="true">
    <rect x="1" y="3" width="20" height="18" rx="3" fill="#e85aa0"/>
    <rect x="3" y="8" width="16" height="11" rx="1" fill="#fbe3ef"/>
    <rect x="5" y="1" width="2" height="4" fill="#e85aa0"/><rect x="15" y="1" width="2" height="4" fill="#e85aa0"/>
    <g fill="#e85aa0"><rect x="5" y="10" width="3" height="3"/><rect x="9.5" y="10" width="3" height="3"/><rect x="14" y="10" width="3" height="3"/><rect x="5" y="14" width="3" height="3"/><rect x="9.5" y="14" width="3" height="3"/><rect x="14" y="14" width="3" height="3"/></g>
  </svg>
  <p class="abs meta" style="left:157px;top:554px">4-5 Months | Starts Nov 2025</p>

  <!-- Topics -->
  <p class="abs topic-title" style="left:538px;top:417px">Topics Include</p>
  <span class="dot" style="left:541px;top:467px"></span><p class="abs topic" style="left:560px;top:458px">Computers</p>
  <span class="dot" style="left:541px;top:502px"></span><p class="abs topic" style="left:560px;top:493px">Marketing</p>
  <span class="dot" style="left:541px;top:536px"></span><p class="abs topic" style="left:560px;top:527px">Sales</p>
  <span class="dot" style="left:541px;top:571px"></span><p class="abs topic" style="left:560px;top:562px">Finance</p>
  <span class="dot" style="left:541px;top:605px"></span><p class="abs topic" style="left:560px;top:596px">Healthcare</p>
  <span class="dot" style="left:541px;top:640px"></span><p class="abs topic" style="left:560px;top:631px">Business Strategy</p>
  <span class="dot" style="left:541px;top:674px"></span><p class="abs topic" style="left:560px;top:665px">Communication</p>
  <span class="dot" style="left:541px;top:709px"></span><p class="abs topic" style="left:560px;top:700px">LedgerPro</p>
  <span class="dot" style="left:541px;top:743px"></span><p class="abs topic" style="left:560px;top:734px">Investments</p>
  <span class="dot" style="left:541px;top:778px"></span><p class="abs topic" style="left:560px;top:769px">Real Estate</p>
  <span class="dot" style="left:541px;top:812px"></span><p class="abs topic" style="left:560px;top:803px">Accounting</p>
  <span class="dot" style="left:541px;top:847px"></span><p class="abs topic" style="left:560px;top:838px">Software</p>

  <!-- Bookkeeping -->
  <h3 class="abs band-title" style="left:121px;top:615px">Bookkeeping &amp; LedgerPro</h3>
  <p class="abs lead" style="left:121px;top:679px">Train for a Quality Job or Manage</p>
  <p class="abs lead" style="left:121px;top:709px">Your Books</p>
  <span class="dot" style="left:124px;top:756px"></span><p class="abs item" style="left:144px;top:747px">Finance Management</p>
  <span class="dot" style="left:124px;top:789px"></span><p class="abs item" style="left:144px;top:780px">Customer &amp; Vendor Management</p>
  <span class="dot" style="left:124px;top:822px"></span><p class="abs item" style="left:144px;top:813px">Advanced Tools</p>
  <svg class="icon" style="left:121px;top:859px" width="28" height="26" viewBox="0 0 28 26" aria-hidden="true">
    <path d="M7 2h14v6a7 7 0 0 1-14 0z" fill="#e8453c"/>
    <path d="M7 4H2c0 5 3 7 6 7M21 4h5c0 5-3 7-6 7" fill="none" stroke="#e8453c" stroke-width="2"/>
    <rect x="12.5" y="14" width="3" height="5" fill="#e8453c"/>
    <rect x="8" y="19" width="12" height="4" rx="1" fill="#e8453c"/>
  </svg>
  <p class="abs meta" style="left:157px;top:859px">5 Weeks | Starts Nov 2025</p>

  <!-- Office suite -->
  <h3 class="abs band-title" style="left:121px;top:918px">Office Suite &amp; Computer Basics</h3>
  <p class="abs lead" style="left:122px;top:982px">The New Job Prerequisite</p>
  <div class="app-row">
    <span class="app app-bullet">Spreadsheets</span>
    <span class="app">Documents</span>
    <span class="app">Email</span>
    <span class="app app-bullet">Slides</span>
  </div>
  <svg class="icon" style="left:124px;top:1065px" width="32" height="30" viewBox="0 0 32 30" aria-hidden="true">
    <rect x="1" y="1" width="30" height="21" rx="2" fill="#1c4a78"/>
    <rect x="3" y="3" width="26" height="17" fill="#2f82d0"/>
    <rect x="14" y="22" width="4" height="4" fill="#1c4a78"/>
    <rect x="9" y="26" width="14" height="3" rx="1" fill="#1c4a78"/>
  </svg>
  <p class="abs meta" style="left:167px;top:1067px;font-size:24.5px">Computer Lab Available for Practice</p>
  <svg class="icon" style="left:123px;top:1111px" width="22" height="22" viewBox="0 0 22 22" aria-hidden="true">
    <rect x="1" y="3" width="20" height="18" rx="3" fill="#e85aa0"/>
    <rect x="3" y="8" width="16" height="11" rx="1" fill="#fbe3ef"/>
    <rect x="5" y="1" width="2" height="4" fill="#e85aa0"/><rect x="15" y="1" width="2" height="4" fill="#e85aa0"/>
    <g fill="#e85aa0"><rect x="5" y="10" width="3" height="3"/><rect x="9.5" y="10" width="3" height="3"/><rect x="14" y="10" width="3" height="3"/><rect x="5" y="14" width="3" height="3"/><rect x="9.5" y="14" width="3" height="3"/><rect x="14" y="14" width="3" height="3"/></g>
  </svg>
  <p class="abs meta" style="left:157px;top:1110px">5 Weeks | Starts Dec 2025</p>
</body>
</html>
```